Roll up corner and Three fold flyer

I need a roll up corner and a three-fold flyer that follow the same design:

I would like to advertise Hospitality, Tourism and Culinary internships in China, Spain, and Australia.

I am attaching some samples:

1.- A roll up corner sample
2.- 4 picuters of a Three-Fold flyer of a company who also does internships in Hospitality. And I really like its flyers.
3.- Three PDF files (Australia, Spain and China) with basic information I would like in the three fold or/and the roll up corner.

Three fold size: A normal letter format
Roll up corner: 85cm x 200 cm

Target Market(s)

Students

Industry/Entity Type

Tourism

Requirements
Must have
• Company name: Northwind Ventures

```html
<!DOCTYPE html>
<html lang="es">
<head>
<meta charset="utf-8">
<title>Northwind Ventures – Roll up</title>
<link href="https://fonts.googleapis.com/css2?family=Fira+Sans+Condensed:ital,wght@0,600;0,700;1,300&family=Montserrat:wght@700&display=swap" rel="stylesheet">
<style>
  :root {
    --stage: #e4e4e4;
    --paper: #f7f7f7;
    --ink: #2b2b2b;
    --panel-dark: #2e2d2e;
    --silver-light: #f2f2f2;
    --silver-dark: #a9a9a9;
    --caption: #d9d9d9;
    --sky: #8fc3d6;
    --city: #3d5f6a;
    --city-deep: #1f3038;
  }
  html, body {
    margin: 0;
    padding: 0;
    width: 1200px;
    height: 1200px;
    overflow: hidden;
    background: var(--stage);
  }
  .rollup {
    position: absolute;
    left: 360px;
    top: 35px;
    width: 480px;
    height: 1130px;
    display: block;
  }
  .kicker {
    font-family: "Montserrat", sans-serif;
    font-weight: 700;
    font-size: 14px;
    letter-spacing: 1px;
    fill: var(--ink);
  }
  .headline {
    font-family: "Fira Sans Condensed", sans-serif;
    font-weight: 700;
    font-size: 46px;
    letter-spacing: 1.5px;
    fill: var(--ink);
  }
  .contact-lead {
    font-family: "Fira Sans Condensed", sans-serif;
    font-weight: 600;
    font-size: 12px;
    letter-spacing: 2.5px;
    fill: var(--ink);
  }
  .contact-email {
    font-family: "Fira Sans Condensed", sans-serif;
    font-weight: 700;
    font-size: 17px;
    letter-spacing: 2.5px;
    fill: var(--ink);
  }
  .claim {
    font-family: "Fira Sans Condensed", sans-serif;
    font-style: italic;
    font-weight: 300;
    font-size: 22px;
    fill: var(--caption);
  }
  .social-name {
    font-family: "Fira Sans Condensed", sans-serif;
    font-weight: 600;
    font-size: 13px;
    fill: var(--caption);
  }
  .social-dot { fill: var(--caption); }
</style>
</head>
<body>
<svg class="rollup" viewBox="0 0 480 1130" xmlns="http://www.w3.org/2000/svg">
  <defs>
    <linearGradient id="cityTone" x1="0" y1="0" x2="0" y2="1">
      <stop offset="0" stop-color="var(--sky)"/>
      <stop offset="0.28" stop-color="#6f98a5"/>
      <stop offset="0.6" stop-color="var(--city)"/>
      <stop offset="1" stop-color="var(--city-deep)"/>
    </linearGradient>
    <linearGradient id="silver" x1="0" y1="0" x2="1" y2="1">
      <stop offset="0" stop-color="var(--silver-light)"/>
      <stop offset="0.55" stop-color="#d2d2d2"/>
      <stop offset="1" stop-color="var(--silver-dark)"/>
    </linearGradient>
  </defs>

  <!-- banner sheet -->
  <rect class="sheet" x="0" y="0" width="480" height="1130" fill="var(--paper)"/>

  <!-- header -->
  <text class="kicker" x="240" y="52" text-anchor="middle">HOSPITALITY INTERNSHIPS</text>
  <rect x="42" y="71" width="396" height="5" fill="var(--ink)"/>
  <text class="headline" x="240" y="136" text-anchor="middle">NORTHWIND VENTURES</text>
  <rect x="42" y="160" width="396" height="5" fill="var(--ink)"/>

  <!-- photo area -->
  <polygon class="photo-area" role="img"
           aria-label="Fotografía: ciudad al atardecer con globos de chat luminosos y un mayordomo sonriente señalando con la mano"
           points="241,189 480,189 480,622 0,994 0,455"
           fill="url(#cityTone)"/>

  <!-- contact diagonal -->
  <g transform="translate(40,425) rotate(-47)">
    <text class="contact-lead" x="0" y="-34">PARA MÁS INFORMACIÓN</text>
    <text class="contact-lead" x="22" y="-20">CONTÁCTANOS A</text>
    <text class="contact-email" x="0" y="0">INFO@NORTHWIND-VENTURES.ORG</text>
  </g>

  <!-- dark lower panel -->
  <polygon class="panel-dark" points="0,994 480,622 480,1130 0,1130" fill="var(--panel-dark)"/>

  <!-- silver diamonds -->
  <polygon class="diamond" points="228,640 326,738 228,836 130,738" fill="url(#silver)"/>
  <polygon class="diamond" points="422,686 458,722 422,758 386,722" fill="url(#silver)"/>

  <!-- claim -->
  <text class="claim" x="240" y="952" text-anchor="middle" transform="rotate(-3 240 952)">EL FORO MERIDIA NOMBRÓ A AUSTRALIA EL</text>
  <text class="claim" x="240" y="985" text-anchor="middle" transform="rotate(-3 240 985)">PAÍS CON LA MEJOR CALIDAD DE VIDA</text>

  <!-- social -->
  <g class="social">
    <circle class="social-dot" cx="110" cy="1045" r="5"/>
    <text class="social-name" x="120" y="1050">Circlo</text>
    <rect class="social-dot" x="212" y="1036" width="10" height="10"/>
    <text class="social-name" x="228" y="1047">Workline</text>
    <circle class="social-dot" cx="330" cy="1045" r="5"/>
    <text class="social-name" x="340" y="1050">Chirpy</text>
  </g>
</svg>
</body>
</html>
```